Re jig a A4 Instructional Flyer

We need an established A4 instructional Flyer (2 pages x A4) - to be rejigged in Harcourt College of Learning Branding to look fresh and new.

Permissions have been received to rejig this Medical Triage Chart. Fresh branding and setting out (fonts) required.

FOOTER NOTES : to be inserted at the bottom of the A4 instruction sheet

Harcourt College produced with permissions from Outback Care Alliance, produced by Outback Care Alliance with Clinic Circle Uptown with permissions from Southern Lakes Carewell Hub. Harcourt acknowledges the NBFPS Standards Criterion 3.2.3 Practice Training and Education in Triage

Target Market(s)

Medical Practices

Industry/Entity Type

Health

Font styles to use
Serif

Colors
0255a3
f78f20

Requirements
Must have
• Professional
• Pops of colour in the chart.
• This chart is to be USED and is VISUAL (no boring grey words throughout)
• PROBS SANS SERIF but SERIF for titles OK
Nice to have
• look at www.harcourtlearn.edu.au FOR BRANDING look and feel

```html
<!DOCTYPE html>
<html lang="en">
<head>
<meta charset="utf-8">
<title>Triage: A guide to urgency – Harcourt College of Learning</title>
<link rel="stylesheet" href="https://fonts.googleapis.com/css2?family=Roboto:wght@300;400;700;900&family=Libre+Baskerville:wght@400;700&display=swap">
<style>
  :root{
    --blue:#0255a3;
    --orange:#f78f20;
    --peach:#fde8d3;
    --mist:#d6e1ee;
    --navy:#1d3461;
    --white:#ffffff;
  }
  *{box-sizing:border-box;margin:0;padding:0}
  html,body{width:1200px;height:848px;overflow:hidden;background:var(--white)}
  body{position:relative;font-family:'Roboto',Arial,sans-serif;color:var(--navy)}

  .brand{position:absolute;left:26px;top:48px;width:214px;display:flex;flex-direction:column;align-items:center;gap:14px}
  .brand-name{font-family:'Libre Baskerville',Georgia,serif;font-size:19px;line-height:1.15;color:var(--navy);text-align:center;letter-spacing:.5px}
  .brand-mark{width:120px;height:120px;background:var(--blue)}

  .headline{position:absolute;left:265px;top:34px;width:900px;font-weight:900;font-size:35px;line-height:37px;color:var(--orange);letter-spacing:-.3px}
  .headline .lead{color:var(--blue)}

  .flow-box{position:absolute;background:var(--peach);border:1.5px solid var(--orange);font-size:11.5px;display:flex;align-items:center;justify-content:center;text-align:center;color:#111}
  .flow-box.strong{font-weight:700}
  .q-urgent{left:266px;top:129px;width:204px;height:23px}
  .q-dontknow{left:266px;top:172px;width:204px;height:23px}
  .q-next{left:266px;top:213px;width:204px;height:38px;line-height:14px;font-size:11px}
  .a-yes{left:499px;top:129px;width:40px;height:22px}
  .a-no{left:499px;top:227px;width:40px;height:22px}

  .record{position:absolute;left:569px;top:129px;width:327px;height:122px;background:var(--peach);border:1.5px solid var(--orange);padding:8px 10px;font-size:10.6px;line-height:15.5px;color:#111}
  .record h2{font-size:11.5px;font-weight:700;line-height:15px;margin-bottom:1px}
  .record ul,.eap ul{list-style:none}
  .record li::before,.eap li::before{content:"• "}

  .eap{position:absolute;left:908px;top:129px;width:252px;height:122px;background:var(--mist);border:2px solid var(--blue);padding:6px 8px;font-size:9.6px;line-height:13.4px;color:#111}
  .eap h2{font-size:14.5px;font-weight:700;color:var(--orange);line-height:18px;margin-bottom:2px}
  .eap li{padding-left:8px;text-indent:-8px}
  .eap .call{margin-top:5px;font-weight:700;font-size:10.5px;color:var(--blue)}
  .eap .call span{color:var(--orange)}

  .arrows{position:absolute;left:0;top:0;width:1200px;height:300px;pointer-events:none}

  .chart{position:absolute;left:27px;top:283px;width:1134px;display:grid;
    grid-template-columns:118px repeat(6,1fr);grid-template-rows:28px 242px 66px 53px 53px;column-gap:6px;row-gap:7px}
  .cell{color:var(--white);font-size:12.8px;font-weight:300;line-height:17.2px;padding:6px 7px}
  .cell.b{background:var(--blue)}
  .cell.o{background:var(--orange);color:#1a1a1a}
  .cell.head{font-weight:700;font-size:13.8px;line-height:16px;display:flex;align-items:center;padding:0 8px;color:var(--white)}
  .cell.o.head{color:#1a1a1a}
  .cell ul{list-style:none}
  .cell li{padding-left:9px;text-indent:-9px}
  .cell li::before{content:"• "}
  .cell.side{color:#cfe0f3}

  .footnote{position:absolute;left:0;top:780px;width:1200px;text-align:center;font-size:12.6px;line-height:17.5px;color:var(--blue);font-weight:300}
</style>
</head>
<body>

<header class="brand">
  <div class="brand-name">Harcourt College<br>of Learning</div>
  <div class="brand-mark"></div>
</header>

<h1 class="headline"><span class="lead">Triage:</span> A guide to urgency for non-clinical staff in general practice for telephone and walk in presentations</h1>

<svg class="arrows" viewBox="0 0 1200 300" aria-hidden="true">
  <g stroke="#f78f20" stroke-width="1.6" fill="none">
    <path d="M470 140 H494"/><path d="M539 140 H563"/>
    <path d="M368 152 V166"/><path d="M368 195 V207"/>
    <path d="M470 238 H494"/><path d="M539 238 H563"/>
  </g>
  <g fill="#f78f20">
    <path d="M498 140 l-6 -4 v8z"/><path d="M568 140 l-6 -4 v8z"/>
    <path d="M368 171 l-4 -6 h8z"/><path d="M368 212 l-4 -6 h8z"/>
    <path d="M498 238 l-6 -4 v8z"/><path d="M568 238 l-6 -4 v8z"/>
  </g>
</svg>

<div class="flow-box strong q-urgent">Do you have an urgent problem?</div>
<div class="flow-box strong a-yes">YES</div>
<div class="flow-box strong q-dontknow">NO / I DON’T KNOW</div>
<div class="flow-box q-next">The next available appointment…<br>Is it okay?</div>
<div class="flow-box strong a-no">NO</div>

<section class="record">
  <h2>Record the patient’s phone number</h2>
  <ul>
    <li>What is the name and age of the patient?</li>
    <li>What is the nature of the problem?</li>
    <li>What is the duration of the problem?</li>
    <li>What is the severity of the problem?</li>
    <li>Has the patient had any previous major health problems?</li>
    <li>Select a category below and follow instructions.</li>
  </ul>
</section>

<section class="eap">
  <h2>EMERGENCY ACTION PLAN</h2>
  <ul>
    <li>Remain calm and do not panic.</li>
    <li>Be aware and respond to the needs of the emergency.</li>
    <li>Assess which patient needs to take priority.</li>
    <li>Deal with any injury or illness in order of severity.</li>
  </ul>
  <p class="call"><span>CALL 000</span> FOR AMBULANCE, POLICE OR FIRE</p>
</section>

<main class="chart">
  <div class="cell b head">INSTRUCTION</div>
  <div class="cell o head">CATEGORY 1</div>
  <div class="cell b head">CATEGORY 2</div>
  <div class="cell o head">CATEGORY 3</div>
  <div class="cell b head">CATEGORY 4</div>
  <div class="cell o head">CATEGORY 5</div>
  <div class="cell b head">CATEGORY 6</div>

  <div class="cell b side">Practice to ask the patient or caller to describe the problem/s, and categorise accordingly:</div>
  <div class="cell o"><ul><li>Chest pain</li><li>Breathing difficulties/ trouble talking</li><li>Facial swelling and rash</li><li>Collapse/altered consciousness</li><li>Facial/limb weakness</li><li>Extensive burns</li><li>Sick patient you have concerns about</li></ul></div>
  <div class="cell b"><ul><li>Fitting</li><li>Bleeding (heavy or persistent)</li><li>Spinal or head injury/ trauma</li><li>Snake bite</li><li>Heart palpitations</li><li>In labour/ruptured membranes</li><li>Neck stiffness/altered consciousness</li></ul></div>
  <div class="cell o"><ul><li>Unable to urinate</li><li>Unwell ‘floppy’ infant</li><li>Poisoning/overdose</li><li>Eye injuries/chemical in the eye</li><li>Pain (severe)</li><li>Injured limb/possible fracture</li></ul></div>
  <div class="cell b"><ul><li>Unwell child/elder with fever, vomiting, diarrhoea or pain for &gt;24 hours</li><li>Pregnancy: pain or bleeding; reduced foetal movement</li><li>Abuse or assault</li><li>Visual disturbance</li><li>Patient or carer with extreme concern</li><li>Psychological distress</li></ul></div>
  <div class="cell o"><ul><li>Unwell child/elderly with fever, vomiting, diarrhoea or pain for &lt;24 hours</li><li>Rash (severe)</li><li>Cut/laceration</li><li>Severe flu like symptoms</li></ul></div>
  <div class="cell b"><ul><li>Adult with fever, but otherwise well</li><li>Post op problems</li><li>Eye or ear infections/ pain</li><li>Adult with continuous vomiting and/or diarrhoea for &gt;24 hrs</li></ul></div>

  <div class="cell b side">Tell the caller to:</div>
  <div class="cell o">Call 000</div>
  <div class="cell b">Go to emergency department now</div>
  <div class="cell o">Put call through to nurse/ doctor</div>
  <div class="cell b">Come to surgery now Advise the on-call nurse/ doctor</div>
  <div class="cell o">Come to surgery today and call back if gets worse</div>
  <div class="cell b">Make an appointment within 24 hours and call back if gets worse</div>

  <div class="cell b side">Practice/ Receptionist</div>
  <div class="cell o">Call nurse/doctor for help immediately</div>
  <div class="cell b">Interrupt nurse/doctor immediately</div>
  <div class="cell o">Advise nurse/doctor now</div>
  <div class="cell b">Discuss with nurse/doctor</div>
  <div class="cell o">Inform nurse/doctor within 30 minutes</div>
  <div class="cell b">Inform nurse/doctor</div>

  <div class="cell b side">Practice/ Receptionist</div>
  <div class="cell o">Retrieve patient file Document activity</div>
  <div class="cell b">Retrieve patient file Document activity</div>
  <div class="cell o">Retrieve patient file Document activity</div>
  <div class="cell b">Retrieve patient file Document activity</div>
  <div class="cell o">Retrieve patient file Document activity</div>
  <div class="cell b">Retrieve patient file Document activity</div>
</main>

<footer class="footnote">
  Harcourt College produced with permissions from Outback Care Alliance, produced by Outback Care Alliance with Clinic Circle Uptown with permissions from Southern Lakes Carewell Hub.<br>
  Harcourt acknowledges the NBFPS Standards Criterion 3.2.3 Practice Training and Education in Triage
</footer>

</body>
</html>
```